Verlune Magician

I want the business card for my business to give to people who watch that later I will be employed to show magic here is my website http://www.verlunemagicien-exemple.fr/I want the interesting design , i am very opened for formal and informal, I watch a lot of design so don't stick to the common shape and form but i hope it can also be produced the thing to write on will be the same as in picture that i will upload , i also will upload the logo for you that so can be easy to useDenis CostilleMagicianMAGICIAN VERLUNE 17 rue des Tilleuls - 25000 BESANÇON contact@verlunemagicien-exemple.fr tel. 0381 476 093 tel. 0664 219 570

```html
<!DOCTYPE html>
<html lang="fr">
<head>
<meta charset="utf-8">
<title>Verlune Magicien – Carte de visite</title>
<link rel="stylesheet" href="https://fonts.googleapis.com/css2?family=Lato:wght@300;400&display=swap">
<style>
  :root {
    --page-bg: #e4e4e4;
    --card-bg: #f5f5f4;
    --ink: #1a1a1a;
    --ink-soft: #3a3a3a;
    --accent: #c8161d;
    --portrait-dark: #111111;
    --portrait-light: #5a5a5a;
  }
  * { margin: 0; padding: 0; box-sizing: border-box; }
  html, body {
    width: 1200px; height: 900px; overflow: hidden;
    background: var(--page-bg);
    font-family: "Lato", sans-serif;
  }
  .card {
    position: absolute;
    left: 80px; top: 153px;
    width: 1040px; height: 594px;
    background: var(--card-bg);
    box-shadow: 0 2px 6px rgba(0,0,0,0.12);
  }
  .brand-portrait {
    position: absolute;
    left: 52px; top: 27px;
    width: 218px; height: 275px;
    background: linear-gradient(170deg, var(--portrait-light) 0%, var(--portrait-dark) 45%, var(--portrait-dark) 100%);
    border-radius: 40px 40px 6px 6px;
  }
  .brand-name {
    position: absolute;
    left: 52px; top: 300px;
    width: 218px;
    text-align: center;
    font-weight: 300;
    font-size: 48px;
    letter-spacing: 1px;
    color: var(--ink);
  }
  .holder {
    position: absolute;
    right: 54px; top: 236px;
    text-align: right;
  }
  .holder-name {
    font-weight: 400;
    font-size: 40px;
    color: var(--accent);
    line-height: 1;
  }
  .holder-role {
    margin-top: 20px;
    font-weight: 300;
    font-size: 30px;
    letter-spacing: 1px;
    color: var(--ink-soft);
    line-height: 1;
  }
  .contacts {
    position: absolute;
    right: 54px; top: 384px;
    list-style: none;
  }
  .contact-row {
    display: flex;
    justify-content: flex-end;
    align-items: center;
    height: 39.5px;
    font-size: 24px;
    font-weight: 400;
    color: var(--ink);
  }
  .contact-icon {
    width: 22px; height: 22px;
    margin-left: 18px;
    fill: var(--accent);
  }
  .studio {
    position: absolute;
    left: 54px; top: 468px;
    font-size: 24px;
    line-height: 31px;
  }
  .studio-name { color: var(--accent); font-weight: 400; }
  .studio-address { color: var(--ink); font-weight: 400; }
</style>
</head>
<body>
  <main class="card">
    <div class="brand-portrait" role="img" aria-label="Illustration en noir et blanc du magicien en veste tenant une carte à jouer"></div>
    <div class="brand-name">VERLUNE</div>

    <header class="holder">
      <h1 class="holder-name">LUCIEN MARBEC</h1>
      <p class="holder-role">MAGICIAN</p>
    </header>

    <ul class="contacts">
      <li class="contact-row">0381 476 093
        <svg class="contact-icon" viewBox="0 0 24 24" aria-hidden="true">
          <path d="M6.6 10.8c1.4 2.8 3.8 5.1 6.6 6.6l2.2-2.2c.3-.3.7-.4 1-.2 1.1.4 2.3.6 3.6.6.6 0 1 .4 1 1V20c0 .6-.4 1-1 1C10.6 21 3 13.4 3 4c0-.6.4-1 1-1h3.5c.6 0 1 .4 1 1 0 1.3.2 2.5.6 3.6.1.3 0 .7-.2 1L6.6 10.8z"/>
          <path d="M14 3a7 7 0 0 1 7 7h-2a5 5 0 0 0-5-5V3zm0 3.5a3.5 3.5 0 0 1 3.5 3.5h-2A1.5 1.5 0 0 0 14 8.5v-2z"/>
        </svg>
      </li>
      <li class="contact-row">0664 219 570
        <svg class="contact-icon" viewBox="0 0 24 24" aria-hidden="true">
          <path d="M2 8c2.5-2.5 6-3.5 10-3.5S19.5 5.5 22 8l-3 2.5-2.5-1.5V7.5c-1.4-.4-2.9-.6-4.5-.6s-3.1.2-4.5.6V9L5 10.5 2 8z"/>
          <path d="M7 11h10l3 9H4l3-9zm5 2.3a2.7 2.7 0 1 0 0 5.4 2.7 2.7 0 0 0 0-5.4z"/>
        </svg>
      </li>
      <li class="contact-row">contact@verlunemagicien-exemple.fr
        <svg class="contact-icon" viewBox="0 0 24 24" aria-hidden="true">
          <path d="M2 5h20v14H2V5zm3 3v8h2.5v-4.5L12 15l4.5-3.5V16H19V8h-1.5L12 12.3 6.5 8H5z"/>
        </svg>
      </li>
      <li class="contact-row">www.verlunemagicien-exemple.fr
        <svg class="contact-icon" viewBox="0 0 24 24" aria-hidden="true">
          <path d="M12 2a10 10 0 1 0 0 20 10 10 0 0 0 0-20zm0 2c1 0 2.2 2.2 2.6 5H9.4C9.8 6.2 11 4 12 4zm-3.8.9A13 13 0 0 0 7.4 9H4.6a8 8 0 0 1 3.6-4.1zM4 12c0-.7.1-1.4.3-2h3a17 17 0 0 0 0 4h-3c-.2-.6-.3-1.3-.3-2zm.6 3h2.8c.2 1.6.6 3 1.2 4.1A8 8 0 0 1 4.6 15zM12 20c-1 0-2.2-2.2-2.6-5h5.2c-.4 2.8-1.6 5-2.6 5zm2.8-6H9.2a15 15 0 0 1 0-4h5.6a15 15 0 0 1 0 4zm.6 5.1c.6-1.1 1-2.5 1.2-4.1h2.8a8 8 0 0 1-4 4.1zM16.7 14a17 17 0 0 0 0-4h3c.2.6.3 1.3.3 2s-.1 1.4-.3 2h-3zm-.1-5a13 13 0 0 0-.8-4.1A8 8 0 0 1 19.4 9h-2.8z"/>
        </svg>
      </li>
    </ul>

    <address class="studio">
      <span class="studio-name">MAGICIAN VERLUNE</span><br>
      <span class="studio-address">17 rue des Tilleuls - 25000 BESANÇON</span>
    </address>
  </main>
</body>
</html>
```